Flyer for a Business Consultant

I need a one-page description of services. I am a Brennick Certifed Talents Mentor. I do not have a personal website but think I will soon purchase this template https://varlowskins.example/skins/lectern/. I like the larger font, simplicity and larger font. I will attach his pricing flyer which I like - not to overly guide or restrict your creative thinking, but only to give a little perspective. I don't like busy, noisy - I like clarity, simplicity. Here 's the Brennick website which these same traits https://www.brennicktalentshub.example/ and can be a source of ideas and colors.

Target Market(s)

CEOs and Middle Managers in organizations

Industry/Entity Type

Financial Service

Colors

Designer to choose colors to be used in the design.

Requirements
Must have
• Clarity, simplicity, but also strength (not weak or frilly looking)
Nice to have
• Warm color(s), larger/not skinny font
Should not have
• Loud, noisy, busy

```html
<!DOCTYPE html>
<html lang="en">
<head>
<meta charset="utf-8">
<title>Strength-Based Team Effectiveness Flyer</title>
<link rel="stylesheet" href="https://fonts.googleapis.com/css2?family=Exo+2:wght@300;400;600;700;800&display=swap">
<style>
  :root {
    --page-bg: #ffffff;
    --flyer-grey: #8e8e8e;
    --photo-light: #b9b9b9;
    --photo-dark: #6f6f6f;
    --band-green: #4b5f2a;
    --fold-green: #3a4a1f;
    --arrow-green: #55702c;
    --ink-white: #ffffff;
    --ink-dark: #2f2f2f;
    --badge-white: #f4f4f4;
  }
  * { margin: 0; padding: 0; box-sizing: border-box; }
  html, body { width: 1200px; height: 971px; overflow: hidden; background: var(--page-bg); }
  body { position: relative; font-family: "Exo 2", Arial, sans-serif; color: var(--ink-white); }

  .flyer { position: absolute; left: 270px; top: 52px; width: 670px; height: 868px; background: var(--flyer-grey); }
  .hero-photo {
    position: absolute; left: 0; top: 0; width: 670px; height: 370px;
    background: radial-gradient(ellipse at 50% 45%, var(--photo-light) 0%, #9d9d9d 45%, var(--flyer-grey) 80%),
                linear-gradient(180deg, var(--photo-dark), var(--flyer-grey));
    background-blend-mode: multiply;
  }
  .headline {
    position: absolute; left: 0; width: 670px; top: 42px; text-align: center;
    font-weight: 800; font-size: 58px; line-height: 58px; letter-spacing: 1px;
    text-shadow: 2px 2px 3px rgba(0,0,0,.45);
  }
  .tagline {
    position: absolute; left: 0; width: 670px; top: 278px; text-align: center;
    font-weight: 700; font-size: 33px; text-shadow: 2px 2px 3px rgba(0,0,0,.4);
  }
  .benefits { position: absolute; left: 0; width: 670px; top: 332px; list-style: none; text-align: center; }
  .benefits li { font-weight: 700; font-size: 13.5px; line-height: 20px; text-shadow: 1px 1px 2px rgba(0,0,0,.3); }
  .benefits svg { width: 15px; height: 10px; vertical-align: 0; margin-right: 4px; }

  .ribbon { position: absolute; left: 0; top: 366px; width: 670px; height: 372px; }
  .services { position: absolute; left: 25px; top: 400px; width: 620px; height: 320px; }
  .service { position: absolute; left: 28px; width: 480px; }
  .service h2 { font-weight: 700; font-size: 24px; line-height: 26px; }
  .service p { font-weight: 300; font-size: 10.6px; line-height: 15px; margin-top: 2px; }
  .service--individual { top: 16px; }
  .service--workshop { top: 108px; }
  .service--followon { top: 212px; }
  .service-icon { position: absolute; left: 525px; width: 58px; height: 58px; background: rgba(255,255,255,.85); border-radius: 4px; }
  .service-icon--individual { top: 18px; }
  .service-icon--workshop { top: 110px; }
  .service-icon--followon { top: 212px; }

  .credential-badge { position: absolute; left: 232px; top: 730px; width: 206px; height: 56px; background: var(--badge-white); border: 1px solid #d0d0d0; }
  .coach-name { position: absolute; left: 0; width: 670px; top: 792px; text-align: center; color: var(--ink-dark); font-weight: 700; font-size: 15px; letter-spacing: 1.5px; }
  .coach-title { position: absolute; left: 0; width: 670px; top: 809px; text-align: center; color: var(--ink-dark); font-size: 8.5px; }

  .contact-bar { position: absolute; left: 0; top: 824px; width: 670px; height: 44px; background: var(--band-green);
    display: flex; justify-content: center; align-items: center; gap: 18px; font-weight: 700; font-size: 17px; }
  .contact-item { display: flex; align-items: center; gap: 6px; }
  .contact-item svg { width: 20px; height: 20px; }
</style>
</head>
<body>
  <main class="flyer">
    <div class="hero-photo" role="img" aria-label="Black and white photo of team members stacking hands together in the centre"></div>
    <h1 class="headline">A STRENGTH-BASED<br>APPROACH TO<br>MANAGING TEAM<br>EFFECTIVENESS</h1>
    <p class="tagline">We help teams grow stronger by:</p>
    <ul class="benefits">
      <li><svg viewBox="0 0 15 10"><path d="M0 3h8V0l7 5-7 5V7H0z" fill="var(--arrow-green)"/></svg>Bringing a deep awareness of their strengths and the strengths of their associates.</li>
      <li><svg viewBox="0 0 15 10"><path d="M0 3h8V0l7 5-7 5V7H0z" fill="var(--arrow-green)"/></svg>Increasing the Team's communication and sense of partnership.</li>
      <li><svg viewBox="0 0 15 10"><path d="M0 3h8V0l7 5-7 5V7H0z" fill="var(--arrow-green)"/></svg>Improving employee engagement and effectiveness.</li>
    </ul>

    <svg class="ribbon" viewBox="0 0 670 372" aria-hidden="true">
      <polygon points="0,0 25,34 25,354 0,372" fill="var(--fold-green)"/>
      <polygon points="670,0 645,34 645,354 670,372" fill="var(--fold-green)"/>
      <rect x="25" y="34" width="620" height="320" fill="var(--band-green)"/>
    </svg>

    <section class="services">
      <article class="service service--individual">
        <h2>INDIVIDUAL SESSIONS</h2>
        <p>Conversational feedback and coaching sessions based on Brennick's Keystone Talents assessments. These sessions last about an hour and lead to a personalized translation of the results and how their strengths show up in their work and inherent blind spots they bring.</p>
      </article>
      <div class="service-icon service-icon--individual" role="img" aria-label="Icon of a presenter at a board"></div>

      <article class="service service--workshop">
        <h2>STRENGTH DISCOVERY WORKSHOP</h2>
        <p>A retreat-style Team Workshop in which the team learns each other's unique Top 5 strengths. The session is very interactive and provides a common language that leads to improved communication and effectiveness. Tailored in 2,3 and 4-hour options are tailored to your Team's challenges and opportunities.</p>
      </article>
      <div class="service-icon service-icon--workshop" role="img" aria-label="Icon of joined hands in a circle"></div>

      <article class="service service--followon">
        <h2>FOLLOW-ON MODULES</h2>
        <p>Follow-on is important to make the insights learned to be practical and integrated into the Teams' approach and workflows. In a debrief session included as part of the workshop, we provide several 15-minute exercise modules for use in regular meetings, and we offer guest facilitated modules of 30- 60 minutes each.</p>
      </article>
      <div class="service-icon service-icon--followon" role="img" aria-label="Icon of three stacked cubes"></div>
    </section>

    <div class="credential-badge" role="img" aria-label="Brennick Certifed Talents Mentor credential badge"></div>
    <p class="coach-name">DORIAN MAXWELL</p>
    <p class="coach-title">Brennick Workplace Talents Mentor</p>

    <footer class="contact-bar">
      <span class="contact-item">
        <svg viewBox="0 0 20 20"><circle cx="10" cy="10" r="10" fill="#fff"/><rect x="4.5" y="6.5" width="11" height="7.5" fill="var(--band-green)"/><path d="M4.5 6.5l5.5 4.5 5.5-4.5" fill="none" stroke="#fff" stroke-width="1.2"/></svg>
        dorian@talentsmeridian.example
      </span>
      <span class="contact-item">
        <svg viewBox="0 0 20 20"><circle cx="10" cy="10" r="10" fill="#fff"/><path d="M6.5 4.5l2.3 2.6-1.2 1.6c.8 1.7 2 2.9 3.7 3.7l1.6-1.2 2.6 2.3-1.4 2c-4.6-.4-8.2-4-8.6-8.6z" fill="var(--band-green)"/></svg>
        615-555-0142
      </span>
    </footer>
  </main>
</body>
</html>
```